Mock up Blog Design for midwife that works in a hospital setting

We are looking to have a design created for a midwife. This blog will be used to share information or experiences related to pregnancy, child birth and motherhood with its readership. It should convey a feeling of warmth and security to women who are looking for a partner in the birthing processes.

We are asking you to design the layout, not code it up. This is a concept project only.

NOtes from the midwife

​So I'm just going to put in links to a few blogs and say what I like and don't like about each one:

rosalindpeverell.com.au/blog/

I like how there is a colorful background that has to do with her books; maybe mine could have a background with baby stuff in the background. It's also nice how there's an index of recent postings with the subject listed and how the postings are sorted by date, all on the same page.

www.steadybottlebrigade.com

I like that this one is set up like a website with tabs for resources, a bio, reader comments, etc.

cradlecorner.tendrilfoundation.org

This blog has a very calming color scheme, which is welcoming. I like that there's a picture for every posting, and that at the bottom of the posting there is a little glossary with the subjects that are covered in the posting. Also, I like the way that the date of each blog is done.

bellyhumourhub.blogspot.com

This one is really funny, and similar in intention to the one that I want to do. I like that she has a glossary of medical terms so that readers can look them up.

General comments:
I'm not sure how much DKWH wants their logo on my blog or in the blog name...
I would like to be able to vet comments before they appear on the blog, so that if there's an inappropriate one, I can screen it out.
I would also like to be able to see how many people have viewed the site.
Updates

Target Market(s)

Pregnant mothers, new moms, hopeful moms

Industry/Entity Type

Hospital

Requirements
Must have
• Incorporation of the logo and at least one of the photographs that will be provided In the header
Should not have
• Should not look canned, rigid or boxy.

```html
<!DOCTYPE html>
<html lang="en">
<head>
<meta charset="utf-8">
<title>Dawnlight – blog for a housewife</title>
<link href="https://fonts.googleapis.com/css2?family=Open+Sans:wght@400;600;700&family=Dancing+Script:wght@500;600&display=swap" rel="stylesheet">
<style>
:root{
  --pink-bg:#c46a95;
  --pink-deep:#b0467a;
  --pink-btn:#a73a6d;
  --plum:#8c2c5a;
  --teal:#4d7d94;
  --teal-dark:#3c6a80;
  --orange:#f0913a;
  --sidebar:#e7e6e7;
  --text:#666;
  --rule:#dcdcdc;
  --white:#fff;
}
*{box-sizing:border-box;margin:0;padding:0}
html,body{width:1200px;height:2899px;overflow:hidden}
body{position:relative;background:radial-gradient(ellipse at 80% 35%,#d687ae 0%,var(--pink-bg) 45%,#b95d8a 100%);font-family:"Open Sans",Arial,sans-serif;color:var(--text)}
.abs{position:absolute}
/* header */
.topbar{position:absolute;left:0;top:0;width:1200px;height:100px;background:linear-gradient(#fff,#ececec);box-shadow:0 2px 6px rgba(0,0,0,.2)}
.brand{position:absolute;display:flex;align-items:center;gap:8px}
.brand-dot{width:34px;height:34px;border-radius:50%;background:var(--pink-deep)}
.brand-name{font-family:"Open Sans",sans-serif;font-weight:600;font-size:20px;color:var(--teal)}
.tagline{position:absolute;left:245px;top:38px;width:560px;white-space:nowrap;font-family:"Dancing Script",cursive;font-weight:500;font-size:18px;line-height:24px;color:var(--teal)}
.user-btn{position:absolute;top:35px;height:32px;border-radius:16px;background:linear-gradient(#c3588a,var(--pink-btn));color:#fff;font-size:11px;font-weight:700;text-align:center;line-height:32px;width:127px;box-shadow:0 1px 2px rgba(0,0,0,.3)}
.welcome{position:absolute;left:102px;top:138px;color:#fff;font-size:32px;font-weight:700;white-space:nowrap}
.welcome span{font-family:"Dancing Script",cursive;font-weight:500;font-size:26px}
.search{position:absolute;left:788px;top:139px;width:312px;height:32px;border-radius:16px;background:#fff;font-size:11px;color:#888;line-height:32px;padding-left:18px}
.search svg{position:absolute;right:12px;top:9px}
/* nav */
.nav{position:absolute;left:108px;top:207px;width:992px;height:46px;display:flex}
.nav a{flex:1;text-decoration:none;color:#fff;font-size:12px;font-weight:600;text-align:center;line-height:46px;background:linear-gradient(#6a98ad,var(--teal-dark));border-right:1px solid #9fbccb;text-transform:uppercase;white-space:nowrap}
.nav a.active{background:linear-gradient(#d36b9c,var(--pink-btn))}
.nav a.signup{background:linear-gradient(#f7a656,var(--orange));border-right:0}
/* content */
.main{position:absolute;left:100px;top:253px;width:673px;height:2458px;background:#fff}
.sidebar{position:absolute;left:773px;top:253px;width:328px;height:2458px;background:var(--sidebar)}
.hero{position:absolute;left:114px;top:270px;width:641px;height:377px;border-radius:6px;background:linear-gradient(160deg,#ece8e0 0%,#b8a8a0 45%,#8a3a3a 100%);overflow:hidden}
.hero-caption{position:absolute;left:0;bottom:0;width:100%;height:77px;background:rgba(40,40,40,.72);color:#fff;font-weight:700;font-size:16px;line-height:26px;padding:13px 20px;text-transform:uppercase}
.hero-dots{position:absolute;right:14px;bottom:12px;display:flex;gap:6px}
.hero-dots i{width:14px;height:14px;border-radius:50%;background:rgba(255,255,255,.35)}
.post{position:absolute;left:114px;width:634px}
.date{position:absolute;left:0;top:0;width:66px;height:89px;border:1px solid #ddd;border-radius:4px;text-align:center;background:#fff}
.date .d{display:block;color:var(--plum);font-size:25px;font-weight:700;line-height:32px;margin-top:3px}
.date .m{display:block;color:var(--teal);font-size:14px;font-weight:700;line-height:15px;border-bottom:1px solid #ddd;padding-bottom:6px;margin:0 8px}
.date .y{display:block;color:#555;font-size:13px;font-weight:700;line-height:28px}
.post-body{margin-left:95px}
.post-title{color:var(--plum);font-size:18px;font-weight:700;line-height:24px}
.post-meta{display:flex;justify-content:space-between;font-size:11px;color:var(--pink-deep);margin-top:6px;padding-bottom:12px;border-bottom:1px solid var(--rule)}
.post-meta .counts{display:flex;gap:14px}
.post-meta svg,.comment .meta svg{vertical-align:-2px;margin-right:4px}
.post-text{font-size:11.5px;line-height:23.5px;margin-top:13px}
.media{position:relative;margin-top:24px;height:356px;margin-bottom:18px}
.play{position:absolute;left:50%;top:50%;width:60px;height:60px;margin:-30px 0 0 -30px;border-radius:50%;background:rgba(50,50,50,.75)}
.play::after{content:"";position:absolute;left:24px;top:18px;border-left:18px solid #fff;border-top:12px solid transparent;border-bottom:12px solid transparent}
.btn{display:inline-block;height:32px;line-height:32px;border-radius:16px;background:linear-gradient(#c3588a,var(--pink-btn));color:#fff;font-size:11px;font-weight:700;text-transform:uppercase;padding:0 32px;box-shadow:0 1px 2px rgba(0,0,0,.3);margin-top:18px;white-space:nowrap}
.sep{position:absolute;left:209px;width:539px;height:1px;background:var(--rule)}
.pager{position:absolute;left:366px;top:2658px;display:flex;gap:7px}
.pager span{height:26px;min-width:26px;border:1px solid #ccc;border-radius:3px;font-size:11px;font-weight:600;color:#555;line-height:24px;text-align:center;padding:0 8px;background:linear-gradient(#fff,#eee)}
/* sidebar */
.widget-head{position:absolute;left:792px;width:309px;height:37px;background:linear-gradient(#5a8aa0,var(--teal-dark));border-radius:6px 0 0 6px;color:#fff;font-size:12.5px;font-weight:700;line-height:37px;padding-left:42px;text-transform:uppercase}
.widget-head::before{content:"";position:absolute;left:12px;top:10px;width:17px;height:17px;border-radius:50%;background:#fff}
.widget-head::after{content:"";position:absolute;left:18px;top:14px;border-left:7px solid var(--teal-dark);border-top:5px solid transparent;border-bottom:5px solid transparent}
.side-title{color:var(--teal);font-size:11.5px;font-weight:700;text-transform:uppercase;line-height:20px}
.side-text{font-size:11px;line-height:22px;color:#777}
.avatar{position:absolute;left:860px;top:359px;width:166px;height:166px;border-radius:50%;background:radial-gradient(circle at 50% 40%,#d9a88e,#8a5d4a 70%,#4a3028);border:3px solid #fff}
.news-item{position:absolute;left:802px;width:290px;display:flex;gap:14px}
.thumb{width:106px;height:83px;flex:none;border-radius:3px}
.archives{position:absolute;left:812px;top:1264px;width:270px;list-style:none}
.archives li{height:34.4px;line-height:34px;font-size:11px;color:#777;border-bottom:1px solid #d6d6d6;padding-left:18px;position:relative}
.archives li::before{content:"›";position:absolute;left:0;color:#999;font-size:14px}
.comment{position:absolute;left:810px;width:280px}
.comment .meta{font-size:10.5px;color:var(--pink-deep);display:flex;gap:14px;margin-top:2px}
.input{position:absolute;left:810px;top:2291px;width:266px;height:32px;border-radius:16px;background:#f5f5f5;border:1px solid #d5d5d5;font-size:11px;color:#777;line-height:30px;padding-left:20px}
.social-box{position:absolute;left:798px;top:2403px;width:282px;height:223px;background:#fff;border:1px solid #c5c5c5}
.social-box .sq{width:40px;height:40px;background:linear-gradient(#c9c3c0,#8d8784)}
/* footer */
.footer-links{position:absolute;left:305px;top:2774px;display:flex;gap:26px;color:#fff;font-size:11.5px}
.copy{position:absolute;left:305px;top:2806px;color:#fff;font-size:11px}
.connect{position:absolute;left:746px;top:2788px;color:#fff;font-size:11px}
.social{position:absolute;left:927px;top:2781px;display:flex;gap:10px}
.social i{width:28px;height:28px;border-radius:50%;background:#fff}
</style>
</head>
<body>

<header class="topbar">
  <div class="brand" style="left:93px;top:33px"><span class="brand-dot"></span><span class="brand-name">Dawnlight</span></div>
  <p class="tagline">Share information or experiences related to pregnancy, child birth and motherhood.</p>
  <a class="user-btn" style="left:835px">USER LOGIN</a>
  <a class="user-btn" style="left:972px">USER REGISTER</a>
</header>

<h1 class="welcome">Welcome to Dawnlight <span>blog for a housewife.</span></h1>
<div class="search">Search by Keyword :
  <svg width="14" height="14" viewBox="0 0 14 14"><circle cx="6" cy="6" r="4.5" fill="none" stroke="#aaa" stroke-width="1.6"/><line x1="9.3" y1="9.3" x2="13" y2="13" stroke="#aaa" stroke-width="1.6"/></svg>
</div>

<nav class="nav">
  <a class="active">Home</a><a>About</a><a>Blog</a><a>Events</a><a>Videos</a><a class="signup">Newsletter Signup</a>
</nav>

<main class="main"></main>
<aside class="sidebar"></aside>

<section class="hero" role="img" aria-label="Photo of a smiling family with parents and four young children">
  <p class="hero-caption">This blog will be used to share information or experiences<br>related to pregnancy, child birth and motherhood</p>
  <div class="hero-dots"><i></i><i></i></div>
</section>

<!-- posts -->
<article class="post" style="top:680px">
  <div class="date"><span class="d">27</span><span class="m">JAN</span><span class="y">2015</span></div>
  <div class="post-body">
    <h2 class="post-title">Caring for your baby's teeth</h2>
    <div class="post-meta"><span>Posted on 27 January 2015</span><span class="counts"><span><svg width="11" height="10" viewBox="0 0 11 10"><path d="M1 1h9v6H4L1 9z" fill="none" stroke="#b0467a" stroke-width="1.2"/></svg>120 Comments</span><span><svg width="10" height="10" viewBox="0 0 10 10"><path d="M1 4h2v5H1zM3 4l3-3.5c1 0 1 1 .6 2.5H9l-.8 6H3z" fill="none" stroke="#b0467a" stroke-width="1"/></svg>84 Likes</span></span></div>
    <p class="post-text">Es simplemente el texto de relleno de las imprentas y archivos de texto. Lorem Ipsum ha sido el texto de relleno estándar de las industrias desde el año 1500, cuando un impresor (N. del T. persona que se dedica a la imprenta) desconocido usó una galería de textos y los mezcló de tal manera que logró hacer un libro de textos especimen. No sólo sobrevivió 500 años, sino que tambien ingresó como texto de relleno en documentos electrónicos, quedando esencialmente...</p>
    <a class="btn">View More Info</a>
  </div>
</article>
<div class="sep" style="top:943px"></div>

<article class="post" style="top:966px">
  <div class="date"><span class="d">27</span><span class="m">JAN</span><span class="y">2015</span></div>
  <div class="post-body">
    <h2 class="post-title">Caring for your baby's teeth</h2>
    <div class="post-meta"><span>Posted on 27 January 2015</span><span class="counts"><span><svg width="11" height="10" viewBox="0 0 11 10"><path d="M1 1h9v6H4L1 9z" fill="none" stroke="#b0467a" stroke-width="1.2"/></svg>120 Comments</span><span><svg width="10" height="10" viewBox="0 0 10 10"><path d="M1 4h2v5H1zM3 4l3-3.5c1 0 1 1 .6 2.5H9l-.8 6H3z" fill="none" stroke="#b0467a" stroke-width="1"/></svg>84 Likes</span></span></div>
    <p class="post-text">Es simplemente el texto de relleno de las imprentas y archivos de texto. Lorem Ipsum ha sido el texto de relleno estándar de las industrias desde el año 1500, cuando un impresor (N. del T. persona que se dedica a la imprenta) desconocido usó una galería de textos.</p>
    <div class="media" role="img" aria-label="Video still of a pregnant woman resting on a sofa" style="background:linear-gradient(135deg,#f2ece8 0%,#d9c2b4 45%,#6d88b8 75%,#e9e4e2 100%)"><span class="play"></span></div>
    <p class="post-text" style="margin-top:0">Es simplemente el texto de relleno de las imprentas y archivos de texto. Lorem Ipsum ha sido el texto de relleno estándar de las industrias desde el año 1500, cuando un impresor (N. del T. persona que se dedica a la imprenta) desconocido usó una galería de textos.</p>
    <a class="btn">View More Info</a>
  </div>
</article>
<div class="sep" style="top:1652px"></div>

<article class="post" style="top:1675px">
  <div class="date"><span class="d">27</span><span class="m">JAN</span><span class="y">2015</span></div>
  <div class="post-body">
    <h2 class="post-title">Caring for your baby's teeth</h2>
    <div class="post-meta"><span>Posted on 27 January 2015</span><span class="counts"><span><svg width="11" height="10" viewBox="0 0 11 10"><path d="M1 1h9v6H4L1 9z" fill="none" stroke="#b0467a" stroke-width="1.2"/></svg>120 Comments</span><span><svg width="10" height="10" viewBox="0 0 10 10"><path d="M1 4h2v5H1zM3 4l3-3.5c1 0 1 1 .6 2.5H9l-.8 6H3z" fill="none" stroke="#b0467a" stroke-width="1"/></svg>84 Likes</span></span></div>
    <p class="post-text">Es simplemente el texto de relleno de las imprentas y archivos de texto. Lorem Ipsum ha sido el texto de relleno estándar de las industrias desde el año 1500, cuando un impresor (N. del T. persona que se dedica a la imprenta) desconocido usó una galería de textos y los mezcló de tal manera que logró hacer un libro de textos especimen. No sólo sobrevivió 500 años, sino que tambien ingresó como texto de relleno en documentos electrónicos, quedando esencialmente...</p>
    <a class="btn">View More Info</a>
  </div>
</article>
<div class="sep" style="top:1936px"></div>

<article class="post" style="top:1959px">
  <div class="date"><span class="d">27</span><span class="m">JAN</span><span class="y">2015</span></div>
  <div class="post-body">
    <h2 class="post-title">Caring for your baby's teeth</h2>
    <div class="post-meta"><span>Posted on 27 January 2015</span><span class="counts"><span><svg width="11" height="10" viewBox="0 0 11 10"><path d="M1 1h9v6H4L1 9z" fill="none" stroke="#b0467a" stroke-width="1.2"/></svg>120 Comments</span><span><svg width="10" height="10" viewBox="0 0 10 10"><path d="M1 4h2v5H1zM3 4l3-3.5c1 0 1 1 .6 2.5H9l-.8 6H3z" fill="none" stroke="#b0467a" stroke-width="1"/></svg>84 Likes</span></span></div>
    <p class="post-text">Es simplemente el texto de relleno de las imprentas y archivos de texto. Lorem Ipsum ha sido el texto de relleno estándar de las industrias desde el año 1500, cuando un impresor (N. del T. persona que se dedica a la imprenta) desconocido usó una galería de textos.</p>
    <div class="media" role="img" aria-label="Video still of hands resting on a pregnant belly" style="background:linear-gradient(160deg,#c9c6cf 0%,#8a8494 40%,#d8cdc8 65%,#6e6a78 100%)"><span class="play"></span></div>
    <p class="post-text" style="margin-top:0">Es simplemente el texto de relleno de las imprentas y archivos de texto. Lorem Ipsum ha sido el texto de relleno estándar de las industrias desde el año 1500...</p>
    <a class="btn">View More Info</a>
  </div>
</article>
<div class="sep" style="top:2622px"></div>

<nav class="pager"><span>Prev</span><span>1</span><span>2</span><span>3</span><span>4</span><span>5</span><span>6</span><span>...</span><span>22</span><span>Next</span></nav>

<!-- sidebar: about -->
<h3 class="widget-head" style="top:294px">About Dawnlight</h3>
<div class="avatar" role="img" aria-label="Portrait photo of the midwife author"></div>
<div class="abs" style="left:800px;top:543px;width:290px;text-align:center">
  <p class="side-title">Es simplemente el texto de relleno</p>
  <p class="side-text" style="margin-top:6px">Es simplemente el texto de relleno de las imprentas y archivos de texto. Lorem Ipsum ha sido el texto de relleno estándar de las industrias desde el año 1500, cuando un impresor...</p>
  <a class="btn" style="margin-top:16px">View More Posts</a>
</div>

<!-- latest news -->
<h3 class="widget-head" style="top:758px">Latest News</h3>
<div class="news-item" style="top:821px"><div class="thumb" role="img" aria-label="Photo of a mother with her child" style="background:linear-gradient(135deg,#e8ddd6,#b67c6c)"></div><div><p class="side-title">Es simplemente el texto de relleno</p><p class="side-text">Es simplemente el texto de relleno de las imprentas...</p></div></div>
<div class="news-item" style="top:927px"><div class="thumb" role="img" aria-label="Photo of a pregnant woman doing yoga outdoors" style="background:linear-gradient(135deg,#a7b86a,#e0d2b8)"></div><div><p class="side-title">Es simplemente el texto de relleno</p><p class="side-text">Es simplemente el texto de relleno de las imprentas...</p></div></div>
<div class="news-item" style="top:1034px"><div class="thumb" role="img" aria-label="Photo of a woman stretching in a park" style="background:linear-gradient(135deg,#7fa24e,#c43a5c)"></div><div><p class="side-title">Es simplemente el texto de relleno</p><p class="side-text">Es simplemente el texto de relleno de las imprentas...</p></div></div>
<a class="btn abs" style="left:802px;top:1114px">View More Posts</a>

<!-- archives -->
<h3 class="widget-head" style="top:1205px">Archives</h3>
<ul class="archives">
  <li>May 2013 (1)</li><li>August 2012 (2)</li><li>March 2012 (1)</li><li>September 2011 (1)</li><li>August 2011 (1)</li><li>June 2011 (1)</li><li>February 2011 (1)</li><li>January 2011 (1)</li><li>August 2010 (1)</li><li>July 2010 (2)</li><li>June 2010 (1)</li><li>May 2010 (1)</li><li>April 2010 (3)</li>
</ul>

<!-- recent comments -->
<h3 class="widget-head" style="top:1735px">Recent Comments</h3>
<div class="comment" style="top:1796px"><p class="side-title">Es simplemente el texto de relleno</p><p class="side-text">Es simplemente el texto de relleno de las imprentas archivos de texto de relleno...</p><p class="meta"><span><svg width="11" height="10" viewBox="0 0 11 10"><path d="M1 1h9v6H4L1 9z" fill="none" stroke="#b0467a" stroke-width="1.2"/></svg>120 Comments</span><span><svg width="10" height="10" viewBox="0 0 10 10"><path d="M1 4h2v5H1zM3 4l3-3.5c1 0 1 1 .6 2.5H9l-.8 6H3z" fill="none" stroke="#b0467a" stroke-width="1"/></svg>84 Likes</span></p></div>
<div class="comment" style="top:1902px"><p class="side-title">Es simplemente el texto de relleno</p><p class="side-text">Es simplemente el texto de relleno de las imprentas archivos de texto de relleno...</p><p class="meta"><span><svg width="11" height="10" viewBox="0 0 11 10"><path d="M1 1h9v6H4L1 9z" fill="none" stroke="#b0467a" stroke-width="1.2"/></svg>120 Comments</span><span><svg width="10" height="10" viewBox="0 0 10 10"><path d="M1 4h2v5H1zM3 4l3-3.5c1 0 1 1 .6 2.5H9l-.8 6H3z" fill="none" stroke="#b0467a" stroke-width="1"/></svg>84 Likes</span></p></div>
<div class="comment" style="top:2008px"><p class="side-title">Es simplemente el texto de relleno</p><p class="side-text">Es simplemente el texto de relleno de las imprentas archivos de texto de relleno...</p><p class="meta"><span><svg width="11" height="10" viewBox="0 0 11 10"><path d="M1 1h9v6H4L1 9z" fill="none" stroke="#b0467a" stroke-width="1.2"/></svg>120 Comments</span><span><svg width="10" height="10" viewBox="0 0 10 10"><path d="M1 4h2v5H1zM3 4l3-3.5c1 0 1 1 .6 2.5H9l-.8 6H3z" fill="none" stroke="#b0467a" stroke-width="1"/></svg>84 Likes</span></p></div>
<a class="btn abs" style="left:802px;top:2098px">View More Comments</a>

<!-- newsletter -->
<h3 class="widget-head" style="top:2195px">Newsletter Signup</h3>
<p class="side-text abs" style="left:812px;top:2250px">Get our recent updates through your email id :</p>
<div class="input">Enter your email id :</div>
<a class="btn abs" style="left:808px;top:2318px">Subscribe Now</a>

<div class="social-box">
  <div class="abs" style="left:8px;top:8px;width:52px;height:46px;background:#333"></div>
  <p class="abs" style="left:68px;top:6px;font-size:12px;font-weight:700;color:var(--teal)">Dawnlight</p>
  <p class="abs" style="left:68px;top:28px;font-size:10px;border:1px solid #ccc;padding:1px 6px;color:#555">Like</p>
  <p class="abs" style="left:8px;top:66px;font-size:10px;color:#555">25,679 people like Brightmarket.</p>
  <div class="abs" style="left:8px;top:84px;display:grid;grid-template-columns:repeat(6,40px);gap:6px">
    <i class="sq"></i><i class="sq"></i><i class="sq"></i><i class="sq"></i><i class="sq"></i><i class="sq"></i>
    <i class="sq"></i><i class="sq"></i><i class="sq"></i><i class="sq"></i><i class="sq"></i><i class="sq"></i>
  </div>
  <p class="abs" style="left:8px;top:200px;font-size:9px;color:#777">Friendwall social plugin</p>
</div>

<!-- footer -->
<div class="brand" style="left:106px;top:2790px"><span class="brand-dot" style="background:#fff"></span><span class="brand-name" style="color:#fff">Dawnlight</span></div>
<div class="abs" style="left:278px;top:2755px;width:1px;height:100px;background:rgba(255,255,255,.4)"></div>
<nav class="footer-links"><span>Home</span><span>/</span><span>About</span><span>/</span><span>Blog</span><span>/</span><span>Events</span><span>/</span><span>Videos</span></nav>
<p class="copy">Copyright © 2015. Dawnlight. All rights reserved.</p>
<p class="connect">Connect with our social network :</p>
<div class="social"><i></i><i></i><i></i><i></i><i></i></div>

</body>
</html>
```